Web Design - 1 page for Buy - Repair - Service - Upgrade - PC Maintenance

We specialize in consumer and small business. It will be mobile friendly, viewable on all devices. Fully editable at the text level of the sections !!! - HTML / CSS only to be able to add a section would be to the web site
Updates

Target Market(s)

consumer and small business IT.

Coding

Coded - Design and coding required

Number of Pages Required

1 page

Font styles to use
Sans Serif

Requirements
Must have
• Looking for a page with a design that compliments the business card and pamphlet that has already been made (attached files). It should look professional and easy to read business. Email and phone number should be visible when the page loads. I do not want any forms for people to mess with. No "Contact Us" form or enter in email for newsletter. Customers will just be looking for this site to confirm we are professionals and have our business in order. OpenStreetMap: embedding map in webpage (like Google Maps) to where the workshop is located
Nice to have
• 2vask.com => this style of website would be more modern visually by integrating higher demands

```html
<!DOCTYPE html>
<html lang="en">
<head>
<meta charset="utf-8">
<title>Nexbyte IT – Computer Repair &amp; Service</title>
<link rel="stylesheet" href="https://fonts.googleapis.com/css2?family=Open+Sans:wght@400;600;700&display=swap">
<style>
  :root {
    --blue: #0a86d6;
    --ink: #3d3d3d;
    --muted: #555;
    --badge: #6b6b6b;
    --band: #eeeeee;
    --white: #ffffff;
  }
  * { box-sizing: border-box; margin: 0; padding: 0; }
  html, body { width: 1200px; height: 2961px; overflow: hidden; }
  body { font-family: "Open Sans", Arial, sans-serif; color: var(--ink); background: var(--white); position: relative; }

  .site-header { position: absolute; top: 0; left: 0; width: 1200px; height: 100px; display: flex; align-items: center; justify-content: space-between; padding: 0 144px; }
  .brand { display: flex; align-items: center; gap: 12px; font-weight: 700; font-size: 30px; color: var(--blue); }
  .brand-mark { width: 26px; height: 26px; background: var(--blue); }
  .header-contact { display: flex; gap: 28px; font-size: 19px; font-weight: 600; color: #555; }
  .contact-item { display: flex; align-items: center; gap: 10px; }
  .contact-icon { width: 36px; height: 36px; border-radius: 50%; background: var(--blue); display: flex; align-items: center; justify-content: center; }

  .hero { position: absolute; top: 100px; left: 0; width: 1200px; height: 384px; background: linear-gradient(100deg, #e9ecef 0%, #d7dce2 35%, #bfc6cf 55%, #7f8fb8 75%, #c9ccdf 100%); }
  .hero-callout { position: absolute; top: 111px; left: 144px; width: 304px; height: 150px; background: var(--blue); color: var(--white); padding: 18px 22px; }
  .hero-kicker { font-size: 19px; font-weight: 600; }
  .hero-title { font-size: 33px; font-weight: 700; line-height: 1.15; margin-top: 4px; }

  .service { position: absolute; left: 144px; width: 912px; height: 217px; display: flex; align-items: center; gap: 28px; }
  .service.reverse { flex-direction: row-reverse; }
  .service-photo { flex: 0 0 217px; height: 217px; border-radius: 50%; }
  .service-text { flex: 1; max-width: 660px; }
  .service.reverse .service-text { margin-right: auto; }
  .service-number { width: 24px; height: 24px; border-radius: 50%; background: var(--badge); color: var(--white); font-size: 13px; font-weight: 700; display: flex; align-items: center; justify-content: center; }
  .service-title { font-size: 26px; font-weight: 600; color: var(--blue); margin: 6px 0; }
  .service-body { font-size: 14px; line-height: 1.5; color: var(--muted); }

  .offer { position: absolute; top: 2355px; left: 0; width: 1200px; height: 237px; background: var(--band); text-align: center; padding-top: 30px; }
  .offer-title { font-size: 27px; font-weight: 600; color: var(--blue); }
  .offer-list { display: flex; justify-content: center; margin-top: 28px; }
  .offer-item { width: 284px; display: flex; flex-direction: column; align-items: center; gap: 14px; font-size: 16px; color: #666; }
  .offer-icon { width: 66px; height: 66px; border-radius: 50%; background: var(--blue); display: flex; align-items: center; justify-content: center; }

  .location-map { position: absolute; top: 2592px; left: 0; width: 1200px; height: 237px; background: linear-gradient(180deg, #c9c9c9, #bdbdbd); }

  .site-footer { position: absolute; top: 2829px; left: 0; width: 1200px; height: 132px; background: var(--blue); color: var(--white); }
  .footer-row { display: flex; justify-content: space-between; align-items: center; padding: 0 144px; height: 88px; }
  .footer-contact { display: flex; gap: 40px; font-size: 20px; font-weight: 600; }
  .footer-contact .contact-icon { background: var(--white); }
  .social { display: flex; gap: 12px; }
  .social-dot { width: 38px; height: 38px; border-radius: 50%; background: var(--white); }
  .footer-rule { margin: 0 144px; border-top: 1px solid rgba(255,255,255,0.3); }
  .copyright { text-align: center; font-size: 11px; font-weight: 600; padding-top: 14px; }
</style>
</head>
<body>
  <header class="site-header">
    <div class="brand"><span class="brand-mark"></span>Nexbyte IT</div>
    <div class="header-contact">
      <div class="contact-item">
        <span class="contact-icon"><svg width="18" height="18" viewBox="0 0 24 24"><path fill="#fff" d="M6.6 10.8a15.1 15.1 0 0 0 6.6 6.6l2.2-2.2c.3-.3.7-.4 1-.2 1.1.4 2.3.6 3.6.6.6 0 1 .4 1 1V20c0 .6-.4 1-1 1A17 17 0 0 1 3 4c0-.6.4-1 1-1h3.5c.6 0 1 .4 1 1 0 1.2.2 2.4.6 3.6.1.3 0 .7-.2 1z"/></svg></span>
        +4210 887 316
      </div>
      <div class="contact-item">
        <span class="contact-icon"><svg width="18" height="18" viewBox="0 0 24 24"><rect x="3" y="5" width="18" height="14" rx="1.5" fill="#fff"/><path d="M3.5 6l8.5 7 8.5-7" fill="none" stroke="#0a86d6" stroke-width="1.8"/></svg></span>
        help@nexbyteit.com
      </div>
    </div>
  </header>

  <section class="hero" role="img" aria-label="Technician in blue gloves repairing an open hard drive beside a laptop">
    <div class="hero-callout">
      <p class="hero-kicker">Have Computer Problems?</p>
      <h1 class="hero-title">GET HELP<br>RIGHT NOW!</h1>
    </div>
  </section>

  <article class="service" style="top:517px">
    <div class="service-photo" role="img" aria-label="Laptop showing quality service graphics" style="background:radial-gradient(circle at 40% 40%, #8fb4d8, #35597d)"></div>
    <div class="service-text">
      <span class="service-number">1</span>
      <h2 class="service-title">Honest Service</h2>
      <p class="service-body">Our certified technicians aren't paid on commission. No pressure to upgrade to products/services you don't need or want. Even the best computers will eventually break down, and if we leave you happy, that's when we hope you'll come back to us.</p>
    </div>
  </article>

  <article class="service reverse" style="top:705px">
    <div class="service-photo" role="img" aria-label="Keyboard with red virus warning" style="background:radial-gradient(circle at 60% 35%, #a4202a, #1a1c24 70%)"></div>
    <div class="service-text">
      <span class="service-number">2</span>
      <h2 class="service-title">Malware/Virus Removal</h2>
      <p class="service-body">Infections can come from many places and sometimes antivirus just isn't enough. We can get your system back to top shape, and train users how to avoid pitfalls in the future, which is better than any antivirus you could buy!</p>
    </div>
  </article>

  <article class="service" style="top:910px">
    <div class="service-photo" role="img" aria-label="Hands repairing a circuit board" style="background:radial-gradient(circle at 45% 50%, #9aa8b4, #4c5a66)"></div>
    <div class="service-text">
      <span class="service-number">3</span>
      <h2 class="service-title">PC/Desktop/Laptop Hardware Repair</h2>
      <p class="service-body">Find out exactly which part of your computer is failing and causing trouble. Our professionals will find the best value replacement and install it, good as new.</p>
    </div>
  </article>

  <article class="service reverse" style="top:1096px">
    <div class="service-photo" role="img" aria-label="Hands typing on a laptop under colourful gear graphics" style="background:radial-gradient(circle at 50% 40%, #6a6a6a, #2c2c2c)"></div>
    <div class="service-text">
      <span class="service-number">4</span>
      <h2 class="service-title">Upgrades</h2>
      <p class="service-body">A new video card to play the latest game at the highest settings? A new disk to give your laptop a very noticeable speed boost? Or maybe just the latest and greatest version of your operating system to keep you secure. We can make the upgrade hassle-free.</p>
    </div>
  </article>

  <article class="service" style="top:1315px">
    <div class="service-photo" role="img" aria-label="Files moving between two folders" style="background:radial-gradient(circle at 50% 50%, #f2b35a 0%, #4fe0c6 45%)"></div>
    <div class="service-text">
      <span class="service-number">5</span>
      <h2 class="service-title">Data Migration</h2>
      <p class="service-body">We can make your new computer feel like an old friend. Transfer all your files, photos, bookmarks, email accounts, personal settings, etc. to a new computer and put them right where you left them.</p>
    </div>
  </article>

  <article class="service reverse" style="top:1504px">
    <div class="service-photo" role="img" aria-label="Laptop with cloud download symbol" style="background:radial-gradient(circle at 50% 35%, #8a8a8a, #3f3f3f)"></div>
    <div class="service-text">
      <span class="service-number">6</span>
      <h2 class="service-title">Data Rescue</h2>
      <p class="service-body">Flash drive formatted? Hard Drive corrupted? Data loss can be devastating, but sometimes recovery is possible for precious photos and important documents. If our best tools can't get your files back, you won't be charged.</p>
    </div>
  </article>

  <article class="service" style="top:1717px">
    <div class="service-photo" role="img" aria-label="Monitor with repair tools" style="background:radial-gradient(circle at 50% 50%, #f6a070, #ef8148)"></div>
    <div class="service-text">
      <span class="service-number">7</span>
      <h2 class="service-title">Tune Ups</h2>
      <p class="service-body">Over time, systems can get slowed down by unnecessary files and programs demanding attention from your processor and memory that should instead be doing work for you! We can clean up (and physically clean out) your system to get it running at peak performance.</p>
    </div>
  </article>

  <article class="service reverse" style="top:1903px">
    <div class="service-photo" role="img" aria-label="Toolbox resting on a keyboard" style="background:radial-gradient(circle at 50% 55%, #b07a45, #1d3556 70%)"></div>
    <div class="service-text">
      <span class="service-number">8</span>
      <h2 class="service-title">In-Home Installation</h2>
      <p class="service-body">All our services come with pick-up and drop-off installation. You won't be left to set up wireless networking, cables, controllers, and printers by yourself.</p>
    </div>
  </article>

  <article class="service" style="top:2098px">
    <div class="service-photo" role="img" aria-label="Digital padlock over network graphics" style="background:radial-gradient(circle at 55% 40%, #6fb0e8, #14294a 75%)"></div>
    <div class="service-text">
      <span class="service-number">9</span>
      <h2 class="service-title">Remote Support</h2>
      <p class="service-body">Small problems shouldn't cost an arm and a leg to fix. We'll set up remote support to your computer to efficiently and cost effectively solve what can be solved without the need of a sending a technician over.</p>
    </div>
  </article>

  <section class="offer">
    <h2 class="offer-title">What We Offer</h2>
    <div class="offer-list">
      <div class="offer-item">
        <span class="offer-icon"><svg width="36" height="36" viewBox="0 0 36 36"><circle cx="18" cy="18" r="12" fill="none" stroke="#fff" stroke-width="6" stroke-dasharray="4.7 4.7"/><circle cx="18" cy="18" r="9" fill="none" stroke="#fff" stroke-width="4"/></svg></span>
        Quick Pc Services
      </div>
      <div class="offer-item">
        <span class="offer-icon"><svg width="36" height="36" viewBox="0 0 36 36"><circle cx="18" cy="18" r="14" fill="none" stroke="#fff" stroke-width="3"/><path d="M18 9v9l6 4" fill="none" stroke="#fff" stroke-width="3" stroke-linecap="round"/></svg></span>
        24/7 Support
      </div>
      <div class="offer-item">
        <span class="offer-icon"><svg width="34" height="34" viewBox="0 0 24 24"><path fill="#fff" d="M2 10h4v11H2zM8 21V10l5-8c1.4 0 2.3 1 2 2.4L14 9h6c1.1 0 2 1 1.8 2.1l-1.6 8.2c-.2.9-1 1.7-2 1.7z"/></svg></span>
        Guaranteed Services
      </div>
    </div>
  </section>

  <section class="location-map" role="img" aria-label="Street map showing the workshop location with a red pin"></section>

  <footer class="site-footer">
    <div class="footer-row">
      <div class="footer-contact">
        <div class="contact-item">
          <span class="contact-icon"><svg width="18" height="18" viewBox="0 0 24 24"><path fill="#0a86d6" d="M6.6 10.8a15.1 15.1 0 0 0 6.6 6.6l2.2-2.2c.3-.3.7-.4 1-.2 1.1.4 2.3.6 3.6.6.6 0 1 .4 1 1V20c0 .6-.4 1-1 1A17 17 0 0 1 3 4c0-.6.4-1 1-1h3.5c.6 0 1 .4 1 1 0 1.2.2 2.4.6 3.6.1.3 0 .7-.2 1z"/></svg></span>
          +4210 887 316
        </div>
        <div class="contact-item">
          <span class="contact-icon"><svg width="18" height="18" viewBox="0 0 24 24"><rect x="3" y="5" width="18" height="14" rx="1.5" fill="#0a86d6"/><path d="M3.5 6l8.5 7 8.5-7" fill="none" stroke="#fff" stroke-width="1.8"/></svg></span>
          help@nexbyteit.com
        </div>
      </div>
      <div class="social">
        <span class="social-dot" aria-label="Social profile"></span>
        <span class="social-dot" aria-label="Social profile"></span>
      </div>
    </div>
    <div class="footer-rule"></div>
    <p class="copyright">© 2019 Nexbyte IT. All Rights Reserved.</p>
  </footer>
</body>
</html>
```